update company powerpoint deck - inject more power/personality into the deck

We would like a designer to provide us with a powerpoint template based on our brand guidelines. Current brand guidelines, colours and existing deck provided.
Current deck lacks punch. We really like our black and white elements - but need options for graphs, tables and charts. We potentially need more supplementary colours to what is currently in our brand guidelines.

Target Market(s)

listed companies - B2B. We are a management consulting company.

Industry/Entity Type

Consulting

Font styles to use
Serif
Sans Serif

Requirements
Must have
• Slides that are common for consulting companies.
The ability to use the deck as a report - not just a presentation format

```html
<!DOCTYPE html>
<html lang="en">
<head>
<meta charset="utf-8">
<title>Kelvane Partners Presentation Template</title>
<link rel="stylesheet" href="https://fonts.googleapis.com/css2?family=Montserrat:wght@500;600;700&family=Arimo:wght@400;700&display=swap">
<style>
:root{
  --board:#aebdc0;
  --paper:#ffffff;
  --mint:#5cfc9e;
  --mint-soft:#9ff5c4;
  --ink:#111418;
  --slate:#4b575d;
  --navy:#141c3c;
  --blue:#3b8ee8;
  --blue-deep:#2e6da4;
  --sky:#b5d3ea;
  --tan:#a0826d;
  --fog:#e4e6e7;
  --grey:#a9a9a9;
  --map:#bdbdbd;
}
*{margin:0;padding:0;box-sizing:border-box}
html,body{width:1200px;height:2433px;overflow:hidden;background:var(--board)}
body{position:relative;font-family:"Arimo",Arial,sans-serif;color:var(--ink)}
.slide{position:absolute;width:512px;height:288px;background:var(--paper);overflow:hidden}
.slide.band::after{content:"";position:absolute;left:0;right:0;bottom:0;height:7px;background:var(--mint)}
.slide.mint{background:var(--mint)}
.col-l{left:71px}.col-r{left:617px}
.abs{position:absolute}
.s-title{position:absolute;left:47px;top:27px;font-family:"Montserrat",sans-serif;font-weight:600;font-size:9px;letter-spacing:2.6px;color:var(--mint)}
.s-brand{position:absolute;right:47px;top:30px;font-family:"Montserrat",sans-serif;font-weight:700;font-size:5px;letter-spacing:.3px;color:var(--ink)}
.brand-lg{font-family:"Montserrat",sans-serif;font-weight:700;font-size:8.5px;letter-spacing:.4px;color:var(--ink)}
.section-title{font-family:"Montserrat",sans-serif;font-weight:700;font-size:13px;letter-spacing:3.6px}
.body{font-size:5.6px;line-height:1.42;color:var(--ink)}
.tiny{font-size:3.8px;line-height:1.3;color:var(--ink)}
.photo{position:absolute}
svg text{font-family:"Arimo",Arial,sans-serif}
</style>
</head>
<body>

<!-- Row 1 -->
<section class="slide col-l" style="top:98px">
  <div class="photo" role="img" aria-label="Black and white photograph of a businessman in a suit holding a newspaper" style="left:0;top:0;width:300px;height:288px;background:linear-gradient(90deg,#6f7275 0%,#a7a9ab 45%,#e9eaeb 80%,#fff 100%)"></div>
  <div class="abs brand-lg" style="left:242px;top:40px">Kelvane Partners</div>
  <div class="abs" style="left:242px;top:100px;font-family:'Montserrat',sans-serif;font-weight:600;font-size:15px;letter-spacing:5px;line-height:1.2;color:var(--mint)">PRESENTATION<br>TITLE HERE</div>
  <p class="abs body" style="left:242px;top:168px;width:230px">Aspernatur magni quae aperiam aut veritati beatae voluptas doloremque perspiciatis error consequuntur ipsa aspernatur iste</p>
  <div class="abs body" style="left:242px;top:256px">www.company.com</div>
</section>

<section class="slide col-r band" style="top:98px">
  <div class="s-title">TEXT WITH CHART</div>
  <div class="s-brand">Kelvane Partners &nbsp;|&nbsp; 2021</div>
  <svg class="abs" style="left:0;top:0" width="512" height="288" viewBox="0 0 512 288" role="img" aria-label="Four grouped bar charts with headlines">
    <g fill="none" stroke="#d6d8d9" stroke-dasharray="1.5 1.5" stroke-width=".6">
      <line x1="171" y1="110" x2="171" y2="252"/><line x1="254" y1="110" x2="254" y2="252"/><line x1="337" y1="110" x2="337" y2="252"/>
    </g>
    <g font-size="3.8">
      <circle cx="106" cy="90" r="5" fill="var(--mint)"/><text x="117" y="89">Lorem ipsum dolar sit</text><text x="117" y="93.5">amet volupta fugit</text>
      <circle cx="189" cy="90" r="5" fill="var(--mint)"/><text x="200" y="89">Aaut illo omnis expli</text><text x="200" y="93.5">nemo ipsam quasi</text>
      <circle cx="272" cy="90" r="5" fill="var(--slate)"/><text x="283" y="89">Dolores ut illo volup</text><text x="283" y="93.5">dolorem perspicia</text>
      <circle cx="355" cy="90" r="5" fill="var(--fog)"/><text x="366" y="89">Beatae magni archi</text><text x="366" y="93.5">aspernatur magni</text>
    </g>
    <g>
      <rect x="106" y="145" width="9" height="34" fill="var(--mint)"/><rect x="118" y="128" width="9" height="51" fill="var(--mint)"/><rect x="130" y="162" width="9" height="17" fill="var(--slate)"/><rect x="142" y="142" width="9" height="37" fill="var(--fog)"/>
      <rect x="189" y="158" width="9" height="21" fill="var(--mint)"/><rect x="201" y="146" width="9" height="33" fill="var(--mint)"/><rect x="213" y="124" width="9" height="55" fill="var(--slate)"/><rect x="225" y="167" width="9" height="12" fill="var(--slate)"/>
      <rect x="272" y="120" width="9" height="59" fill="var(--mint)"/><rect x="284" y="129" width="9" height="50" fill="var(--mint)"/><rect x="296" y="146" width="9" height="33" fill="var(--slate)"/><rect x="308" y="166" width="9" height="13" fill="var(--fog)"/>
      <rect x="355" y="157" width="9" height="22" fill="var(--mint)"/><rect x="367" y="164" width="9" height="15" fill="var(--mint)"/><rect x="379" y="151" width="9" height="28" fill="var(--slate)"/><rect x="391" y="123" width="9" height="56" fill="var(--fog)"/>
    </g>
    <g fill="var(--mint)"><circle cx="131" cy="203" r="13"/><circle cx="213" cy="203" r="13"/><circle cx="296" cy="203" r="13"/><circle cx="378" cy="203" r="13"/></g>
    <g fill="none" stroke="#fff" stroke-width="1">
      <rect x="125" y="198" width="12" height="10" rx="1"/><path d="M125 199l6 5 6-5"/>
      <rect x="207" y="197" width="12" height="12" rx="1"/><path d="M210 206v-3M213 206v-5M216 206v-2"/>
      <rect x="290" y="197" width="12" height="12" rx="1"/><path d="M293 205h6M293 202h6"/>
      <circle cx="378" cy="203" r="5"/><path d="M378 196v3M378 207v3M371 203h3M382 203h3"/>
    </g>
    <g text-anchor="middle" font-size="3.8">
      <text x="131" y="230" fill="var(--mint)" font-size="5.2">HEADLINE</text><text x="131" y="236">Lorem ipsum dolar sit</text><text x="131" y="240.5">amet voluptatem</text>
      <text x="213" y="230" fill="var(--mint)" font-size="5.2">HEADLINE</text><text x="213" y="236">Aaut illo omnis explicabo</text><text x="213" y="240.5">nemo rem ipsam</text>
      <text x="296" y="230" fill="var(--mint)" font-size="5.2">HEADLINE</text><text x="296" y="236">Dolores ut illo voluptatem</text><text x="296" y="240.5">doloremque perspicia</text>
      <text x="378" y="230" fill="var(--mint)" font-size="5.2">HEADLINE</text><text x="378" y="236">Beatae magni architec</text><text x="378" y="240.5">odit aspernatur rem</text>
    </g>
  </svg>
</section>

<!-- Row 2 -->
<section class="slide col-l" style="top:421px">
  <div class="abs brand-lg" style="left:47px;top:43px">Kelvane Partners</div>
  <div class="abs section-title" style="left:47px;top:186px">SECTIO TITLE</div>
  <p class="abs body" style="left:47px;top:209px;width:300px">aspernatur magni quae aperiam aut veritatis beatae eos aut voluptas doloremque perspiciatis error consequuntur ipsa aspernatur iste sit quae explicabo dicta quasi sed enim natus</p>
</section>

<section class="slide col-r band" style="top:421px">
  <div class="s-title">TEXT WITH MAP</div>
  <div class="s-brand">Kelvane Partners &nbsp;|&nbsp; 2021</div>
  <div class="photo" role="img" aria-label="Grey world map with location pins in North America, Europe, Africa and Australia" style="left:103px;top:60px;width:318px;height:145px;background:radial-gradient(ellipse 28% 45% at 24% 45%,var(--map) 0%,var(--map) 70%,transparent 72%),radial-gradient(ellipse 40% 48% at 70% 42%,var(--map) 0%,var(--map) 70%,transparent 72%)"></div>
  <svg class="abs" style="left:0;top:0" width="512" height="288" viewBox="0 0 512 288" role="img" aria-label="Four progress rings: 75, 65, 50 and 35 percent">
    <g fill="none" stroke-width="2.4">
      <circle cx="95" cy="235" r="10" stroke="#e6e8e9"/><circle cx="95" cy="235" r="10" stroke="var(--mint)" stroke-dasharray="47 63" transform="rotate(-90 95 235)"/>
      <circle cx="184" cy="235" r="10" stroke="#e6e8e9"/><circle cx="184" cy="235" r="10" stroke="var(--mint)" stroke-dasharray="41 63" transform="rotate(-90 184 235)"/>
      <circle cx="272" cy="235" r="10" stroke="#e6e8e9"/><circle cx="272" cy="235" r="10" stroke="var(--slate)" stroke-dasharray="31.5 63" transform="rotate(90 272 235)"/>
      <circle cx="356" cy="235" r="10" stroke="#e6e8e9"/><circle cx="356" cy="235" r="10" stroke="var(--blue)" stroke-dasharray="22 63" transform="rotate(90 356 235)"/>
    </g>
    <g font-size="3.8">
      <text x="110" y="231" fill="var(--mint)" font-size="8">75%</text><text x="110" y="238">Lorem ipsum dolar</text><text x="110" y="242">amet volupta fug</text>
      <text x="199" y="231" fill="var(--mint)" font-size="8">65%</text><text x="199" y="238">Aaut illo omnis expl</text><text x="199" y="242">nemo ipsam quasi</text>
      <text x="287" y="231" fill="var(--mint)" font-size="8">50%</text><text x="287" y="238">Dolores ut illo volup</text><text x="287" y="242">dolorem perspicia</text>
      <text x="371" y="231" fill="var(--mint)" font-size="8">35%</text><text x="371" y="238">Beatae magni archi</text><text x="371" y="242">aspernatur magni</text>
    </g>
  </svg>
</section>

<!-- Row 3 -->
<section class="slide col-l mint" style="top:744px">
  <div class="abs brand-lg" style="left:47px;top:43px">Kelvane Partners</div>
  <div class="abs section-title" style="left:47px;top:186px">SECTIO TITLE</div>
  <p class="abs body" style="left:47px;top:209px;width:300px">aspernatur magni quae aperiam aut veritatis beatae eos aut voluptas doloremque perspiciatis error consequuntur ipsa aspernatur iste sit quae explicabo dicta quasi sed enim natus</p>
</section>

<section class="slide col-r band" style="top:744px">
  <div class="s-title">BUSINESS TIMELINE</div>
  <div class="s-brand">Kelvane Partners &nbsp;|&nbsp; 2021</div>
  <div class="abs" style="left:0;right:0;top:61px;text-align:center;font-size:7.4px">Veritatis dicta sunt <span style="color:var(--mint)">quasi</span> eaque rem <span style="color:var(--mint)">aperiams?</span></div>
  <svg class="abs" style="left:0;top:0" width="512" height="288" viewBox="0 0 512 288" role="img" aria-label="Timeline curve with four milestones">
    <path d="M92 245C105 220 115 205 127 197S190 185 220 185 280 160 309 150 370 146 393 143 415 130 420 125" fill="none" stroke="#c9cccd" stroke-width=".7" stroke-dasharray="2 2"/>
    <g stroke="#c9cccd" stroke-width=".6" stroke-dasharray="1.5 1.5"><line x1="127" y1="197" x2="127" y2="132"/><line x1="220" y1="185" x2="220" y2="215"/><line x1="309" y1="150" x2="309" y2="110"/><line x1="393" y1="143" x2="393" y2="175"/></g>
    <circle cx="127" cy="197" r="3.5" fill="var(--mint)"/><circle cx="220" cy="185" r="3.5" fill="#dde0e1"/><circle cx="309" cy="150" r="3.5" fill="var(--slate)"/><circle cx="393" cy="143" r="3.5" fill="var(--mint)"/>
    <g fill="none" stroke="var(--slate)" stroke-width=".7">
      <rect x="91" y="125" width="28" height="21"/><line x1="91" y1="129" x2="119" y2="129"/><path d="M105 141l-5-5a2.5 2.5 0 0 1 5-2 2.5 2.5 0 0 1 5 2z"/>
      <rect x="185" y="218" width="26" height="20"/><line x1="185" y1="222" x2="211" y2="222"/><path d="M193 228h10l-2-2M203 232h-10l2 2"/>
      <path d="M318 104h24v17h-15l-4 4v-4h-5z"/><path d="M322 116l6-5 4 3 6-6"/>
      <path d="M399 170h24v17h-15l-4 4v-4h-5z"/><path d="M405 182v-4M409 182v-6h4v6M415 182v-5h3v5"/>
    </g>
    <g font-size="3.8">
      <text x="137" y="130" font-size="4.8">CONSECTETUR</text><text x="137" y="139" fill="var(--mint)" font-size="5.6">HEADLINE</text><text x="137" y="147">Lorem ipsum dolar amet volupta</text><text x="137" y="151.5">fugit aut illo omnis expli nemo ipsam</text>
      <text x="307" y="107" text-anchor="end" font-size="4.8">CONSECTETUR</text><text x="307" y="116" text-anchor="end" fill="var(--mint)" font-size="5.6">HEADLINE</text><text x="307" y="124" text-anchor="end">Lorem ipsum dolar amet volupta</text><text x="307" y="128.5" text-anchor="end">fugit aut illo omnis expli nemo ipsam</text>
      <text x="391" y="168" text-anchor="end" font-size="4.8">CONSECTETUR</text><text x="391" y="177" text-anchor="end" fill="var(--mint)" font-size="5.6">HEADLINE</text><text x="391" y="185" text-anchor="end">Lorem ipsum dolar amet volupta</text><text x="391" y="189.5" text-anchor="end">fugit aut illo omnis expli nemo ipsam</text>
      <text x="229" y="213" font-size="4.8">CONSECTETUR</text><text x="229" y="222" fill="var(--mint)" font-size="5.6">HEADLINE</text><text x="229" y="230">Lorem ipsum dolar amet volupta</text><text x="229" y="234.5">fugit aut illo omnis expli nemo ipsam</text>
    </g>
  </svg>
</section>

<!-- Row 4 -->
<section class="slide col-l band" style="top:1068px">
  <div class="s-title">ABOUT US</div>
  <div class="s-brand">Kelvane Partners &nbsp;|&nbsp; 2021</div>
  <div class="photo" role="img" aria-label="Black and white photograph of businessmen in a meeting in front of bookshelves" style="left:47px;top:61px;width:419px;height:59px;background:linear-gradient(90deg,#2b2b2b,#8d8d8d 30%,#4a4a4a 55%,#9b9b9b 75%,#333)"></div>
  <p class="abs body" style="left:47px;top:165px;width:419px">Lorem ipsum dolar sit amet voluptatem fugit aut illo omnis explicabo ipsa ipsa, nemo rem ipsam quasi illo dolores ut voluptatem doloremque perspiciatis beatae magni architecto odit odit, aspernatur magni quae aperiam aut veritatis beatae eos aut voluptas doloremque error natus natus, qui aut eaque inventore aut quasi consequuntur consequuntur ipsa aspernatur iste sit sit, quae explicabo dicta quasi sed doloremque sit amet rem eos illo omnis aut aperiam ab ipsam ipsa odit aut aperiam aut aspernatur veritatis unde unde, sed enim accusantium laudantium laudantium sunt perspiciatis ipsam sed doloremque ipsam dolores totam unde, et aut illo aut veritatis explicabo dicta quasi veritatis dicta sunt quasi eaque rem eos enim aperiam aperiam, omnis ipsa sed nemo perspiciatis quasi ipsam eos ratione quia quae ut quia architecto</p>
  <p class="abs body" style="left:47px;top:225px;width:419px">Lorem ipsum dolar sit amet voluptatem fugit aut illo omnis explicabo ipsa ipsa, nemo rem ipsam quasi illo dolores ut voluptatem doloremque perspiciatis beatae magni architecto odit odit, aspernatur magni quae aperiam aut veritatis beatae eos aut.</p>
</section>

<section class="slide col-r band" style="top:1068px">
  <div class="s-title">GALLERY</div>
  <div class="s-brand">Kelvane Partners &nbsp;|&nbsp; 2021</div>
  <div class="abs" style="left:88px;top:72px;width:338px;height:156px;display:grid;grid-template-columns:repeat(4,1fr);grid-template-rows:1fr 1fr;color:#fff;text-align:center;font-size:5.4px;font-weight:700">
    <div style="background:var(--mint);padding-top:22px">VOLUPTAS<br>MAGNI QUAE<div class="tiny" style="color:#fff;font-weight:400;margin-top:8px">Lorem ipsum dolar sit amet<br>voluptatem fugit aut</div></div>
    <div role="img" aria-label="Photograph of hands typing on a laptop" style="background:linear-gradient(135deg,#9fb3ad,#e6ecea 60%,#b8c7c2)"></div>
    <div style="background:var(--fog);color:var(--slate);padding-top:22px">CONSEQU<br>MAGNI QUAE<div class="tiny" style="color:var(--slate);font-weight:400;margin-top:8px">Lorem ipsum dolar sit amet<br>voluptatem fugit aut</div></div>
    <div style="background:var(--navy);padding-top:22px">EOS EXPLICABO<br>VOLUPTAS<div class="tiny" style="color:#fff;font-weight:400;margin-top:8px">Lorem ipsum dolar sit amet<br>voluptatem fugit aut</div></div>
    <div role="img" aria-label="Photograph of a pen pointing at a printed chart" style="background:linear-gradient(135deg,#6b5a55,#d9d3cf 55%,#8a8f94)"></div>
    <div style="background:var(--slate);padding-top:24px">INVENTORE AUT<br>QUASI<div class="tiny" style="color:#fff;font-weight:400;margin-top:8px">Lorem ipsum dolar sit amet<br>voluptatem fugit aut</div></div>
    <div role="img" aria-label="Photograph of a business team smiling in an office" style="grid-column:span 2;background:linear-gradient(90deg,#d9c7a6,#f1efe9 35%,#6f7c8d 65%,#c0c9d2)"></div>
  </div>
</section>

<!-- Row 5 -->
<section class="slide col-l band" style="top:1394px">
  <div class="s-title">ABOUT US</div>
  <div class="s-brand">Kelvane Partners &nbsp;|&nbsp; 2021</div>
  <div class="abs body" style="left:47px;top:61px">Are you experiencing any of these <span style="color:var(--mint)">challenges?</span></div>
  <p class="abs body" style="left:47px;top:78px;width:419px">Lorem ipsum dolar sit amet voluptatem fugit aut illo omnis explicabo ipsa ipsa, nemo rem ipsam quasi illo dolores ut voluptatem doloremque perspiciatis beatae magni architecto odit odit, aspernatur magni quae aperiam aut veritatis beatae eos aut voluptas doloremque error natus natus, qui aut eaque inventore aut quasi consequuntur consequuntur ipsa aspernatur iste sit sit, quae explicabo dicta quasi sed doloremque sit amet rem eos illo omnis aut aperiam ab ipsam ipsa odit aut aperiam aut aspernatur veritatis unde unde, sed enim accusantium laudantium laudantium sunt perspiciatis ipsam sed doloremque ipsam dolores totam unde, et aut illo aut veritatis explicabo dicta quasi veritatis dicta sunt quasi eaque rem eos enim aperiam aperiam, omnis ipsa sed nemo perspiciatis quasi ipsam eos ratione quia quae ut quia architecto</p>
  <p class="abs body" style="left:47px;top:142px;width:419px">Lorem ipsum dolar sit amet voluptatem fugit aut illo omnis explicabo ipsa ipsa, nemo rem ipsam quasi illo dolores ut voluptatem doloremque perspiciatis beatae magni architecto odit odit, aspernatur magni quae aperiam aut veritatis beatae eos aut voluptas doloremque error natus natus, qui aut eaque inventore aut quasi consequuntur consequuntur ipsa aspernatur iste sit sit, quae explicabo dicta quasi sed doloremque sit amet rem eos illo omnis aut aperiam ab ipsam ipsa odit aut aperiam aut aspernatur veritatis unde unde, sed enim accusantium laudantium laudantium sunt perspiciatis ipsam sed doloremque ipsam dolores totam unde, et aut illo aut veritatis explicabo dicta quasi veritatis dicta sunt quasi eaque rem eos enim aperiam aperiam, omnis ipsa sed nemo perspiciatis quasi ipsam eos ratione quia quae ut quia architecto</p>
  <p class="abs body" style="left:47px;top:206px;width:419px">Lorem ipsum dolar sit amet voluptatem fugit aut illo omnis explicabo ipsa ipsa, nemo rem ipsam quasi illo dolores ut voluptatem doloremque perspiciatis beatae magni architecto odit odit, aspernatur magni quae aperiam aut veritatis beatae eos aut voluptas doloremque error natus natus, qui aut eaque inventore aut quasi consequuntur consequuntur</p>
</section>

<section class="slide col-r band" style="top:1394px">
  <div class="s-title">OUR TEAM</div>
  <div class="s-brand">Kelvane Partners &nbsp;|&nbsp; 2021</div>
  <div class="photo" role="img" aria-label="Portrait photograph of a smiling man in a suit" style="left:85px;top:76px;width:65px;height:65px;border-radius:50%;background:radial-gradient(circle at 50% 40%,#d9b59a,#5a6470 70%,#eeeeee)"></div>
  <div class="photo" role="img" aria-label="Portrait photograph of a woman with glasses" style="left:165px;top:76px;width:65px;height:65px;border-radius:50%;background:radial-gradient(circle at 50% 40%,#d9a98a,#3b2e2a 70%,#dcd6cf)"></div>
  <div class="abs" style="left:85px;top:151px;width:65px;text-align:center;font-size:4.4px">MR. JHONE DOE</div>
  <div class="abs" style="left:165px;top:151px;width:65px;text-align:center;font-size:4.4px">MRS. LINDA DOE</div>
  <svg class="abs" style="left:0;top:0" width="512" height="288" viewBox="0 0 512 288" role="img" aria-label="Team headlines and service icons">
    <g fill="none" stroke="var(--slate)" stroke-width=".7">
      <rect x="253" y="100" width="13" height="11"/><path d="M258 103v5l4-2.5z"/>
      <path d="M256 152v-14M256 139h8l-2 3 2 3h-8"/>
      <path d="M353 111v-10l7-2v10"/><circle cx="351" cy="111" r="2"/><circle cx="358" cy="109" r="2"/>
      <path d="M351 138v14M356 138v14M361 138v14"/><circle cx="351" cy="142" r="1.5"/><circle cx="356" cy="147" r="1.5"/><circle cx="361" cy="143" r="1.5"/>
      <polygon points="116,180 134,190 134,210 116,220 98,210 98,190"/>
      <polygon points="210,180 228,190 228,210 210,220 192,210 192,190"/>
      <polygon points="304,180 322,190 322,210 304,220 286,210 286,190"/>
      <polygon points="398,180 416,190 416,210 398,220 380,210 380,190"/>
      <rect x="108" y="192" width="16" height="16"/><line x1="108" y1="197" x2="124" y2="197"/><line x1="114" y1="197" x2="114" y2="208"/>
      <path d="M203 190v16h16M199 194h16v16"/><line x1="201" y1="210" x2="219" y2="190"/>
      <path d="M296 203a8 8 0 0 1 16 0"/><rect x="295" y="202" width="4" height="7" rx="1"/><rect x="309" y="202" width="4" height="7" rx="1"/>
      <circle cx="395" cy="197" r="6"/><line x1="399" y1="201" x2="406" y2="208"/>
    </g>
    <g font-size="3.8">
      <text x="272" y="101" fill="var(--mint)" font-size="5.4">HEADLINE</text><text x="272" y="107">Lorem ipsum dolar sit</text><text x="272" y="111">amet volupta fugit</text>
      <text x="272" y="139" fill="var(--mint)" font-size="5.4">HEADLINE</text><text x="272" y="145">Dolores ut illo volup</text><text x="272" y="149">dolorem perspicia</text>
      <text x="369" y="101" fill="var(--mint)" font-size="5.4">HEADLINE</text><text x="369" y="107">Aaut illo omnis expli</text><text x="369" y="111">nemo ipsam quasi</text>
      <text x="369" y="139" fill="var(--mint)" font-size="5.4">HEADLINE</text><text x="369" y="145">Dolores ut illo volup</text><text x="369" y="149">dolorem perspicia</text>
    </g>
    <g font-size="3.8" text-anchor="middle">
      <text x="116" y="232">Lorem ipsum dolar amet</text><text x="116" y="236.5">volupta fugit aut illo omnis expli</text><text x="116" y="241">nemo ipsam magni</text>
      <text x="210" y="232">Lorem ipsum dolar amet</text><text x="210" y="236.5">volupta fugit aut illo omnis expli</text><text x="210" y="241">nemo ipsam magni</text>
      <text x="304" y="232">Lorem ipsum dolar amet</text><text x="304" y="236.5">volupta fugit aut illo omnis expli</text><text x="304" y="241">nemo ipsam magni</text>
      <text x="398" y="232">Lorem ipsum dolar amet</text><text x="398" y="236.5">volupta fugit aut illo omnis expli</text><text x="398" y="241">nemo ipsam magni</text>
    </g>
  </svg>
</section>

<!-- Row 6 -->
<section class="slide col-l band" style="top:1721px">
  <div class="s-title">TEXT WITH CHART</div>
  <div class="s-brand">Kelvane Partners &nbsp;|&nbsp; 2021</div>
  <svg class="abs" style="left:0;top:0" width="512" height="288" viewBox="0 0 512 288" role="img" aria-label="Pie chart in four quarters with labels">
    <g transform="rotate(45 254 160)">
      <path d="M254 160V88a72 72 0 0 1 72 72z" fill="var(--slate)"/>
      <path d="M254 160h72a72 72 0 0 1-72 72z" fill="var(--mint-soft)"/>
      <path d="M254 160v72a72 72 0 0 1-72-72z" fill="var(--mint)"/>
      <path d="M254 160h-72a72 72 0 0 1 72-72z" fill="var(--fog)"/>
    </g>
    <g fill="none" stroke="var(--slate)" stroke-width=".7"><rect x="249" y="111" width="12" height="14"/><line x1="252" y1="118" x2="258" y2="118"/></g>
    <g fill="none" stroke="#fff" stroke-width=".7"><rect x="288" y="154" width="16" height="11"/><line x1="296" y1="165" x2="296" y2="169"/><rect x="209" y="155" width="16" height="11"/><line x1="209" y1="160" x2="225" y2="160"/><rect x="248" y="197" width="12" height="9" rx="1"/><rect x="253" y="201" width="12" height="9" rx="1"/></g>
    <g fill="none" stroke="#c9cccd" stroke-width=".6" stroke-dasharray="2 2">
      <path d="M150 130L170 118H262"/><path d="M335 120L360 110"/><path d="M160 195L184 185V160"/><path d="M300 236H375L395 215"/>
    </g>
    <g font-size="6" fill="var(--mint)">
      <text x="80" y="101">Lorem ipsum dolar sit</text><text x="90" y="108">amet volupta fugit</text>
      <text x="87" y="167">Aaut illo omnis expli</text><text x="95" y="174">nemo ipsam quasi</text>
      <text x="372" y="101">Beatae magni archi</text><text x="372" y="108">aspernatur magni</text>
      <text x="372" y="167">Dolores ut illo volup</text><text x="372" y="174">dolorem perspicia</text>
    </g>
    <g font-size="3.8">
      <text x="84" y="116">nemo rem ipsam quasi illo dolores</text><text x="86" y="121">ut voluptatem doloremque perspi</text>
      <text x="82" y="182">nemo rem ipsam quasi illo dolores</text><text x="84" y="187">ut voluptatem doloremque perspi</text>
      <text x="372" y="116">nemo rem ipsam quasi illo dolores</text><text x="372" y="121">ut voluptatem doloremque perspi</text>
      <text x="372" y="182">nemo rem ipsam quasi illo dolores</text><text x="372" y="187">ut voluptatem doloremque perspi</text>
    </g>
  </svg>
</section>

<section class="slide col-r band" style="top:1721px">
  <div class="s-title">CLOSING</div>
  <div class="s-brand">Kelvane Partners &nbsp;|&nbsp; 2021</div>
  <div class="photo" role="img" aria-label="Black and white city skyline with tall office towers under a cloudy sky" style="left:0;top:150px;width:512px;height:131px;background:linear-gradient(180deg,#fff 0%,#e7e8e9 35%,#9a9c9e 70%,#3f4245 100%)"></div>
  <div class="abs section-title" style="left:0;right:0;top:88px;text-align:center;font-size:12px;letter-spacing:4.5px">THANK YOU</div>
  <p class="abs tiny" style="left:110px;width:292px;top:124px;text-align:center;font-size:4.6px">aspernatur magni quae aperiam aut veritatis beatae eos aut voluptas doloremque perspiciatis error consequuntur ipsa aspernatur iste sit quae explicabo dicta quasi sed enim natus</p>
  <div class="abs tiny" style="left:0;right:0;top:144px;text-align:center;font-size:4.6px">www.company.com</div>
</section>

<!-- Row 7 -->
<section class="slide col-l band" style="top:2047px">
  <div class="s-title">TEXT WITH CHART</div>
  <div class="s-brand">Kelvane Partners &nbsp;|&nbsp; 2021</div>
  <svg class="abs" style="left:0;top:0" width="512" height="288" viewBox="0 0 512 288" role="img" aria-label="Stacked bar chart and pie chart with legend">
    <g font-size="3.2">
      <circle cx="94" cy="71" r="3.5" fill="var(--navy)"/><text x="101" y="70">Lorem ipsum dolar</text><text x="101" y="74">amet volupta fugit</text>
      <circle cx="150" cy="71" r="3.5" fill="var(--blue)"/><text x="157" y="70">Aaut illo omnis expli</text><text x="157" y="74">nemo ipsam quasi</text>
      <circle cx="210" cy="71" r="3.5" fill="var(--mint)"/><text x="217" y="70">Dolores ut illo volup</text><text x="217" y="74">dolorem perspicia</text>
      <circle cx="266" cy="71" r="3.5" fill="var(--slate)"/><text x="273" y="70">Beatae magni archi</text><text x="273" y="74">aspernatur magni</text>
      <circle cx="324" cy="71" r="3.5" fill="var(--fog)"/><text x="331" y="70">Dolores ut illo volup</text><text x="331" y="74">dolorem perspicia</text>
    </g>
    <g stroke="#d6d8d9" stroke-width=".5" stroke-dasharray="1.5 1.5">
      <line x1="100" y1="91" x2="300" y2="91"/><line x1="100" y1="109" x2="300" y2="109"/><line x1="100" y1="127" x2="300" y2="127"/><line x1="100" y1="145" x2="300" y2="145"/><line x1="100" y1="163" x2="300" y2="163"/><line x1="100" y1="181" x2="300" y2="181"/><line x1="100" y1="199" x2="300" y2="199"/>
    </g>
    <g font-size="3.4" fill="var(--grey)"><text x="86" y="93">7.0</text><text x="86" y="111">6.0</text><text x="86" y="129">5.0</text><text x="86" y="147">4.0</text><text x="86" y="165">3.0</text><text x="86" y="183">2.0</text><text x="86" y="201">1.0</text></g>
    <g>
      <rect x="115" y="91" width="20" height="14" fill="var(--fog)"/><rect x="115" y="105" width="20" height="14" fill="var(--slate)"/><rect x="115" y="119" width="20" height="22" fill="var(--mint)"/><rect x="115" y="141" width="20" height="38" fill="var(--blue)"/><rect x="115" y="179" width="20" height="20" fill="var(--navy)"/>
      <rect x="150" y="91" width="20" height="7" fill="var(--fog)"/><rect x="150" y="98" width="20" height="18" fill="var(--slate)"/><rect x="150" y="116" width="20" height="10" fill="var(--mint)"/><rect x="150" y="126" width="20" height="39" fill="var(--blue)"/><rect x="150" y="165" width="20" height="34" fill="var(--navy)"/>
      <rect x="185" y="91" width="20" height="20" fill="var(--fog)"/><rect x="185" y="111" width="20" height="13" fill="var(--slate)"/><rect x="185" y="124" width="20" height="16" fill="var(--blue)"/><rect x="185" y="140" width="20" height="28" fill="var(--mint)"/><rect x="185" y="168" width="20" height="31" fill="var(--navy)"/>
      <rect x="220" y="91" width="20" height="10" fill="var(--fog)"/><rect x="220" y="101" width="20" height="8" fill="var(--slate)"/><rect x="220" y="109" width="20" height="18" fill="var(--mint)"/><rect x="220" y="127" width="20" height="17" fill="var(--blue)"/><rect x="220" y="144" width="20" height="55" fill="var(--navy)"/>
      <rect x="255" y="91" width="20" height="14" fill="var(--fog)"/><rect x="255" y="105" width="20" height="21" fill="var(--slate)"/><rect x="255" y="126" width="20" height="24" fill="var(--mint)"/><rect x="255" y="150" width="20" height="8" fill="var(--blue)"/><rect x="255" y="158" width="20" height="41" fill="var(--navy)"/>
    </g>
    <g>
      <path d="M380 140V92a48 48 0 0 1 41.6 24z" fill="var(--slate)"/>
      <path d="M380 140l41.6-24a48 48 0 0 1 2 40z" fill="var(--ink)"/>
      <path d="M380 140l43.6 16a48 48 0 0 1-43.6 32z" fill="var(--tan)"/>
      <path d="M380 140v48a48 48 0 0 1-46-36z" fill="var(--sky)"/>
      <path d="M380 140l-46 12a48 48 0 0 1 46-60z" fill="var(--blue-deep)"/>
    </g>
    <g font-size="3.6" fill="var(--slate)" text-anchor="middle"><text x="380" y="200">Lorem ipsum dolor sit amet, consectetur</text><text x="380" y="205">adipiscing elit, sed do eiusmod tempor</text><text x="380" y="210">incididunt ut labore et dolore magna aliqua.</text></g>
    <g fill="none" stroke="var(--slate)" stroke-width=".6">
      <path d="M98 230h14v10h-8l-3 3v-3h-3z"/><path d="M102 237l3-3 2 2 3-3"/>
      <path d="M222 230h14v10h-8l-3 3v-3h-3z"/><path d="M225 234h8M225 237h6"/>
      <path d="M346 230h14v10h-8l-3 3v-3h-3z"/><path d="M350 237v-2M353 237v-4M356 237v-3"/>
    </g>
    <g font-size="3.8">
      <text x="120" y="234">Lorem ipsum dolar sit</text><text x="120" y="238.5">amet volupta fugit</text>
      <text x="244" y="234">Aaut illo omnis expli</text><text x="244" y="238.5">nemo ipsam quasi</text>
      <text x="368" y="234">Dolores ut illo volup</text><text x="368" y="238.5">dolorem perspicia</text>
    </g>
  </svg>
</section>

</body>
</html>
```